Just Sold Postcard

Real Estate/ Bramwell Oakes Realty.I'd like a template that I can use to change out the picture of the home, verbiage on the front, and address. I'm including a picture of what I've used in the past. I like designs that use red, with some blue and white. I'd like the ability to change the verbiage on the back as well.

Industry/Entity Type

Real Estate

Font styles to use
Serif
Sans Serif

```html
<!DOCTYPE html>
<html lang="en">
<head>
<meta charset="UTF-8">
<title>Just Sold Postcard – Bramwell Oakes Realty</title>
<link rel="stylesheet" href="https://fonts.googleapis.com/css2?family=EB+Garamond:wght@400&family=Open+Sans:wght@400;600&display=swap">
<style>
  :root {
    --page-bg: #e9e7e4;
    --card-white: #ffffff;
    --brand-red: #c0202f;
    --accent-red: #e03a2f;
    --brand-navy: #27307a;
    --blue-start: #2b3a9a;
    --blue-end: #12306a;
    --line-grey: #c9c9c9;
    --photo-sky: #cfd6dc;
    --photo-house: #7d6c5c;
    --photo-lawn: #4e6b3a;
    --text-white: #ffffff;
  }
  * { margin: 0; padding: 0; box-sizing: border-box; }
  html, body { width: 874px; height: 1200px; overflow: hidden; }
  body {
    background: var(--page-bg);
    font-family: "Open Sans", Arial, sans-serif;
    position: relative;
  }
  .postcard {
    position: absolute;
    width: 651px;
    height: 503px;
    background: var(--card-white);
    box-shadow: 0 2px 8px rgba(0,0,0,0.18);
    overflow: hidden;
  }

  /* Front */
  .postcard--front { left: 82px; top: 60px; }
  .front-photo {
    position: absolute; left: 0; top: 0; width: 651px; height: 324px;
    background: linear-gradient(180deg, var(--photo-sky) 0%, #b9b2a8 30%, var(--photo-house) 60%, #6a5d50 82%, var(--photo-lawn) 100%);
  }
  .front-banner {
    position: absolute; left: 0; top: 324px; width: 651px; height: 78px;
    background: var(--brand-red);
  }
  .front-banner .headline {
    position: absolute; left: 42px; top: 4px;
    font-family: "EB Garamond", Georgia, serif;
    font-size: 62px; line-height: 70px; color: var(--text-white);
    letter-spacing: 0.5px;
  }
  .front-banner .address {
    position: absolute; left: 414px; top: 38px;
    font-size: 17px; color: var(--text-white);
  }
  .agent-block { position: absolute; left: 45px; top: 407px; }
  .agent-name { font-size: 25px; color: var(--accent-red); line-height: 34px; }
  .agent-tagline { font-size: 17px; color: var(--brand-navy); line-height: 25px; }
  .agent-phone {
    font-size: 17px; color: var(--brand-navy); line-height: 24px;
    display: flex; align-items: center; gap: 5px;
  }
  .brand-mark {
    display: flex; align-items: center; gap: 8px;
    font-family: "Open Sans", Arial, sans-serif;
    font-weight: 600; color: var(--brand-navy);
  }
  .brand-mark .dot {
    width: 14px; height: 14px; border-radius: 50%; background: var(--brand-red);
    flex: none;
  }
  .postcard--front .brand-mark {
    position: absolute; left: 430px; top: 436px; font-size: 19px;
  }

  /* Back */
  .postcard--back { left: 143px; top: 629px; }
  .back-column { position: absolute; left: 0; top: 0; width: 355px; height: 455px; }
  .back-logo-area {
    position: absolute; left: 0; top: 0; width: 232px; height: 138px;
    display: flex; align-items: center; justify-content: center;
  }
  .back-logo-area .brand-mark { font-size: 16px; }
  .back-photo {
    position: absolute; left: 232px; top: 12px; width: 123px; height: 126px;
    background: linear-gradient(180deg, var(--photo-sky) 0%, var(--photo-house) 55%, var(--photo-lawn) 100%);
  }
  .back-feature {
    position: absolute; left: 0; top: 138px; width: 355px; height: 151px;
    background: var(--brand-red); color: var(--text-white);
  }
  .back-feature .address {
    position: absolute; left: 34px; top: 10px;
    display: flex; align-items: center; gap: 18px;
    font-size: 20px;
  }
  .back-feature .description {
    position: absolute; left: 0; top: 58px; width: 355px;
    text-align: center; font-size: 16px; line-height: 24px;
  }
  .back-contact {
    position: absolute; left: 0; top: 289px; width: 355px; height: 162px;
    background: linear-gradient(90deg, var(--blue-start), var(--blue-end));
    color: var(--text-white);
  }
  .back-contact .agent-row {
    position: absolute; left: 32px; top: 24px;
    display: flex; align-items: baseline; gap: 10px;
  }
  .back-contact .agent-row .name { font-size: 24px; }
  .back-contact .agent-row .phone { font-size: 16px; display: flex; align-items: center; gap: 4px; }
  .back-contact .divider {
    position: absolute; left: 0; top: 54px; width: 355px; height: 1px;
    background: rgba(255,255,255,0.12);
  }
  .back-contact .call-to-action {
    position: absolute; left: 0; top: 66px; width: 355px;
    text-align: center; font-size: 12.5px; line-height: 16px;
  }
  .stamp-box {
    position: absolute; left: 546px; top: 23px; width: 90px; height: 72px;
    border: 1.5px solid var(--line-grey);
  }
  .address-lines { position: absolute; left: 392px; top: 185px; width: 238px; }
  .address-lines span {
    display: block; height: 1.5px; background: var(--line-grey); margin-bottom: 36px;
  }
</style>
</head>
<body>

  <section class="postcard postcard--front" aria-label="Postcard front">
    <div class="front-photo" role="img" aria-label="Photo of the sold home: two-storey stone and stucco house at dusk"></div>
    <div class="front-banner">
      <h1 class="headline">JUST SOLD!</h1>
      <p class="address">2716 Maple Crest Lane</p>
    </div>
    <div class="agent-block">
      <p class="agent-name">Dana Whitfield</p>
      <p class="agent-tagline">Your Neighborhood Expert</p>
      <p class="agent-phone">
        <svg width="15" height="15" viewBox="0 0 16 16" aria-hidden="true">
          <circle cx="8" cy="8" r="7" fill="none" stroke="currentColor" stroke-width="1.5"/>
          <path d="M5.2 4.6c.4-.3.9-.2 1.1.2l.6 1.1c.2.3.1.7-.2.9l-.4.3c.3.9 1 1.6 1.9 2l.3-.4c.2-.3.6-.4.9-.2l1.1.6c.4.2.5.7.2 1.1l-.4.5c-.4.4-1 .5-1.5.3-2-.8-3.4-2.3-4.1-4.2-.2-.5 0-1.1.3-1.5z" fill="currentColor"/>
        </svg>
        919 555 0148
      </p>
    </div>
    <div class="brand-mark"><span class="dot"></span>Bramwell Oakes Realty</div>
  </section>

  <section class="postcard postcard--back" aria-label="Postcard back">
    <div class="back-column">
      <div class="back-logo-area">
        <div class="brand-mark"><span class="dot"></span>Bramwell Oakes Realty</div>
      </div>
      <div class="back-photo" role="img" aria-label="Photo of the sold home front entrance"></div>
      <div class="back-feature">
        <p class="address">
          <svg width="14" height="20" viewBox="0 0 14 20" aria-hidden="true">
            <path d="M7 0C3.1 0 0 3.1 0 7c0 5 7 13 7 13s7-8 7-13c0-3.9-3.1-7-7-7zm0 9.6A2.6 2.6 0 1 1 7 4.4a2.6 2.6 0 0 1 0 5.2z" fill="currentColor"/>
          </svg>
          2716 Maple Crest Lane
        </p>
        <p class="description">Fabulous End Unit<br>with granite countertops<br>and hardwood floors. Private lot</p>
      </div>
      <div class="back-contact">
        <div class="agent-row">
          <span class="name">Dana Whitfield</span>
          <span class="phone">
            <svg width="14" height="14" viewBox="0 0 16 16" aria-hidden="true">
              <circle cx="8" cy="8" r="7" fill="none" stroke="currentColor" stroke-width="1.5"/>
              <path d="M5.2 4.6c.4-.3.9-.2 1.1.2l.6 1.1c.2.3.1.7-.2.9l-.4.3c.3.9 1 1.6 1.9 2l.3-.4c.2-.3.6-.4.9-.2l1.1.6c.4.2.5.7.2 1.1l-.4.5c-.4.4-1 .5-1.5.3-2-.8-3.4-2.3-4.1-4.2-.2-.5 0-1.1.3-1.5z" fill="currentColor"/>
            </svg>
            919 555 0148
          </span>
        </div>
        <div class="divider"></div>
        <p class="call-to-action">Contact me today!<br>For a free Market<br>Analysis of your home!<br>919 555 0148 or<br>dana.whitfield@example.com</p>
      </div>
    </div>
    <div class="stamp-box" aria-label="Stamp area"></div>
    <div class="address-lines" aria-label="Mailing address lines">
      <span></span><span></span><span></span><span></span><span></span>
    </div>
  </section>

</body>
</html>
```